Business card for Sports Apparel business

DOUBLE SIDED DESIGN
We need business cards for a new sports apparel business. We are developing a protective headband for soccer initially.
Corvell is focused on designing and developing head protection products to reduce the likelihood of concussion when playing sports. Exploring and understanding medical insights, material science research, current and former players experiences and governing bodies guidelines has allowed Corvell to develop the safety, style, form and function requirements of a suitable product to bring to market.
Target Market(s)
Mums buying kits for the sons and daughters. Amateur footballers.
Industry/Entity Type
Sporting Good
Contact Information for Business Card
Martin Ashgrove - CEO
Mobile: +44 7391608254
Email: martin@corvell.co.uk
Tel: 0208 5143927
Helena Pardoe - COO
Mob: +44 7356 409183
Email: helena@corvell.co.uk
Tel: 0208 5143927
Duncan Wyvern - CCO
Mob: +44 7468 230517
Email: duncan@corvell.co.uk
Tel: 0208 5143927
Look and feel

```html
<!DOCTYPE html>
<html lang="en">
<head>
<meta charset="utf-8">
<title>Corvell Business Card</title>
<link href="https://fonts.googleapis.com/css2?family=Lato:wght@400;700;900&display=swap" rel="stylesheet">
<style>
  :root {
    --brand-blue: #17609a;
    --ink-dark: #2b2b2b;
    --ink-grey: #555a5e;
    --paper: #ffffff;
    --backdrop: #2a2a2a;
    --band-grey: #5f5f5f;
  }
  * { box-sizing: border-box; margin: 0; padding: 0; }
  html, body {
    width: 1200px; height: 878px; overflow: hidden;
    background: var(--backdrop);
    font-family: "Lato", sans-serif;
  }
  .canvas {
    position: relative; width: 1200px; height: 878px;
    display: flex; flex-direction: column; align-items: center; justify-content: center; gap: 48px;
  }
  .card {
    position: relative; width: 580px; height: 331px;
    box-shadow: 0 14px 30px rgba(0,0,0,0.45);
    overflow: hidden;
  }
  /* Front side */
  .card--front {
    background: var(--brand-blue);
    display: flex; flex-direction: column; align-items: center; justify-content: center;
  }
  .front-wordmark {
    display: flex; align-items: center; gap: 16px;
    color: var(--paper); font-weight: 900; font-size: 72px; letter-spacing: 4px; text-transform: uppercase;
  }
  .front-wordmark .mark-square { width: 22px; height: 22px; background: var(--paper); }
  .front-web {
    margin-top: 34px; color: var(--paper); font-size: 15px; letter-spacing: 5px;
  }
  /* Back side */
  .card--back { background: var(--paper); }
  .back-wordmark {
    position: absolute; left: 42px; top: 42px;
    display: flex; align-items: center; gap: 12px;
    color: var(--brand-blue); font-weight: 900; font-size: 42px; letter-spacing: 2px; text-transform: uppercase;
  }
  .back-wordmark .mark-square { width: 14px; height: 14px; background: var(--brand-blue); }
  .contact-list {
    position: absolute; left: 42px; top: 178px; list-style: none;
  }
  .contact-list li {
    display: flex; align-items: center; gap: 14px;
    font-size: 17px; color: var(--ink-dark); height: 26px; font-style: italic;
  }
  .contact-list svg { width: 16px; height: 16px; fill: var(--brand-blue); flex: none; }
  .contact-list .accent { color: var(--brand-blue); }
  .person {
    position: absolute; right: 44px; top: 224px; text-align: right;
  }
  .person-name { font-size: 30px; font-weight: 900; color: var(--brand-blue); line-height: 1; }
  .person-role { margin-top: 6px; font-size: 17px; color: var(--ink-dark); letter-spacing: 1px; }
  .bottom-band {
    position: absolute; left: 0; right: 0; bottom: 0; height: 12px; display: flex; gap: 6px;
  }
  .bottom-band .band-grey { width: 52px; background: var(--band-grey); }
  .bottom-band .band-blue { flex: 1; background: var(--brand-blue); }
</style>
</head>
<body>
<main class="canvas">
  <section class="card card--front" aria-label="Card front">
    <div class="front-wordmark"><span class="mark-square"></span>Corvell</div>
    <p class="front-web">www.corvell.co.uk</p>
  </section>

  <section class="card card--back" aria-label="Card back">
    <div class="back-wordmark"><span class="mark-square"></span>Corvell</div>

    <ul class="contact-list">
      <li>
        <svg viewBox="0 0 16 16" aria-hidden="true"><path d="M1 6c0-2 3-3 7-3s7 1 7 3v1h-3.5V5.5h-7V7H1z"/><rect x="3" y="8" width="10" height="6" rx="1"/></svg>
        0208 5143927
      </li>
      <li>
        <svg viewBox="0 0 16 16" aria-hidden="true"><path d="M4 1h8a1 1 0 0 1 1 1v12a1 1 0 0 1-1 1H4a1 1 0 0 1-1-1V2a1 1 0 0 1 1-1zm1 2v9h6V3z"/></svg>
        +44 7391608254
      </li>
      <li>
        <svg viewBox="0 0 16 16" aria-hidden="true"><path d="M1 3h14v10H1zm1.5 1.2L8 8.5l5.5-4.3z"/></svg>
        martin@corvell.co.uk
      </li>
      <li>
        <svg viewBox="0 0 16 16" aria-hidden="true"><circle cx="8" cy="8" r="7"/><path d="M1 8h14M8 1v14" stroke="#fff" stroke-width="1"/></svg>
        <span>www.<span class="accent">corvell</span>.co.uk</span>
      </li>
    </ul>

    <div class="person">
      <p class="person-name">Martin Ashgrove</p>
      <p class="person-role">CEO</p>
    </div>

    <div class="bottom-band"><span class="band-grey"></span><span class="band-blue"></span></div>
  </section>
</main>
</body>
</html>
```